Peter Lasko-Wren Finance

Need a personal website advertising Equipment Finance,Business Finance,Commercial Finance, Construction Finance, Bridging Finance. Similar websites are www.varoplend.com.au / www.kitmoxa.com.au / www.rzb4.com.au /wwwbelvaxcredit.com.au

Target Market(s)

Business People

Industry/Entity Type

Business

Number of Pages Required

3 page

Font styles to use
Serif
Sans Serif

Requirements
Must have
• All i want is a simple corporate looking website advertising Equipment Finance, Commercial Finance, Construction Finance, Business Finance, Bridging Finance,

```html
<!DOCTYPE html>
<html lang="en">
<head>
<meta charset="utf-8">
<title>Peter Lasko-Wren Finance</title>
<link href="https://fonts.googleapis.com/css2?family=Open+Sans:wght@300;400;600;700&display=swap" rel="stylesheet">
<style>
:root{
  --green:#a3c21f;
  --blue:#2489cc;
  --blue-dark:#1c7bbb;
  --ink:#3a3a3a;
  --text:#6d6d6d;
  --grey-bg:#efefef;
  --line:#d9d9d9;
  --white:#ffffff;
}
*{box-sizing:border-box;margin:0;padding:0}
html,body{width:1200px;height:2440px;overflow:hidden;background:var(--white)}
body{font-family:'Open Sans',Arial,sans-serif;color:var(--text);position:relative}
.abs{position:absolute}

/* hero */
.hero{left:0;top:0;width:1200px;height:712px;background:linear-gradient(100deg,#e6ecf1 0%,#c9d5df 40%,#7f93a6 70%,#3d4f66 100%)}
.site-header{left:0;top:0;width:1200px;height:112px;background:rgba(255,255,255,.82)}
.brand{left:72px;top:36px;font-size:32px;font-weight:400;color:var(--blue);line-height:1.2;white-space:nowrap}
.main-nav{right:72px;top:40px;display:flex;gap:8px}
.main-nav a{font-size:20px;color:var(--blue);text-decoration:none;padding:8px 18px;letter-spacing:.5px}
.main-nav a.active{background:var(--blue);color:var(--white)}
.hero-title{left:72px;top:236px;font-size:44px;font-weight:700;color:var(--green);line-height:1.22;width:560px}
.hero-call{left:72px;top:366px;display:flex;align-items:center;gap:14px;font-size:44px;font-weight:700;color:var(--ink)}
.phone-ring{width:50px;height:50px;border:3px solid var(--ink);border-radius:50%;display:flex;align-items:center;justify-content:center}
.btn{display:inline-block;font-weight:600;color:var(--white);text-decoration:none;font-size:18px;padding:0 26px;line-height:52px}
.btn-green{background:var(--green)}
.btn-blue{background:var(--blue)}
.hero-btn{left:72px;top:440px}

/* green band */
.band{left:0;top:712px;width:1200px;height:144px;background:var(--green)}
.band-text{left:72px;top:46px;font-size:50px;font-weight:300;color:var(--white)}
.band-btn{right:72px;top:46px}

/* services */
.section-title{font-size:52px;font-weight:300;color:var(--green);text-align:center}
.section-title span{color:var(--blue)}
.services-title{left:0;top:895px;width:1200px}
.services-lead{left:250px;top:966px;width:700px;text-align:center;font-size:15px;line-height:1.6}
.service{top:1028px;width:192px;text-align:center}
.service-photo{width:192px;height:132px;background:linear-gradient(135deg,#d8e3ec,#7c94ab)}
.service h3{margin-top:22px;font-size:22px;font-weight:400;color:var(--blue)}
.service p{margin-top:6px;font-size:15px;line-height:1.5}

/* welcome */
.welcome{left:0;top:1340px;width:1200px;height:392px;background:var(--grey-bg)}
.welcome-kicker{left:72px;top:54px;font-size:44px;font-weight:300;color:var(--green);line-height:1;white-space:nowrap}
.welcome-name{left:72px;top:104px;font-size:44px;font-weight:300;color:var(--blue);line-height:1;white-space:nowrap}
.welcome-text{left:72px;top:172px;width:600px;font-size:15px;line-height:1.65}
.welcome-btn{left:72px;top:256px}
.video{left:736px;top:32px;width:384px;height:280px;background:linear-gradient(180deg,#9aa9b8 0%,#4d5f74 60%,#2f3b4b 100%)}
.play{left:162px;top:110px}

/* news & quote */
.col-title{font-size:50px;font-weight:300;color:var(--green);line-height:1}
.col-title span{color:var(--blue)}
.news-title{left:72px;top:1778px}
.news-item{left:72px;width:500px;display:flex;gap:26px}
.date{width:60px;height:62px;background:var(--grey-bg);text-align:center;padding-top:6px;flex:none}
.date b{display:block;font-size:28px;color:var(--blue);line-height:1}
.date small{font-size:11px;color:var(--text)}
.news-body p{font-size:15px;line-height:1.55;color:var(--blue)}
.news-body a{font-size:13px;font-weight:700;color:var(--green);text-decoration:none}
.quote-title{left:628px;top:1778px}
.field{position:absolute;border:1px solid var(--line);background:var(--white);font-size:14px;color:var(--text);padding:10px 12px;height:44px}
.submit{left:628px;top:2134px}

/* footer */
.footer{left:0;top:2260px;width:1200px;height:180px;background:var(--blue-dark)}
.footer-nav{left:72px;top:30px;display:flex;gap:38px}
.footer-nav a{color:var(--white);text-decoration:none;font-size:17px}
.social{right:72px;top:22px;display:flex;gap:14px}
.social span{width:42px;height:42px;border:2px solid var(--white);border-radius:50%;display:block}
.footer-rule{left:72px;top:86px;width:1056px;height:1px;background:rgba(255,255,255,.3)}
.contact-item{top:108px;display:flex;align-items:center;gap:14px;color:var(--white);font-size:14px;line-height:1.4}
.contact-item .dot{width:44px;height:44px;border-radius:50%;background:var(--white);display:flex;align-items:center;justify-content:center;flex:none}
.contact-item.big{font-size:20px;font-weight:700}
</style>
</head>
<body>

<section class="hero abs" role="img" aria-label="Photo of two businessmen reviewing documents at a desk"></section>
<header class="site-header abs">
  <div class="brand abs">Peter Lasko-Wren Finance</div>
  <nav class="main-nav abs">
    <a href="#" class="active">HOME</a><a href="#">ABOUT</a><a href="#">SERVICES</a><a href="#">CONTACT</a>
  </nav>
</header>
<h1 class="hero-title abs">LOREM IPSUM IS SIMPLY DUMMY TEXT.</h1>
<div class="hero-call abs">CALL US
  <span class="phone-ring"><svg width="26" height="26" viewBox="0 0 24 24"><path fill="#3a3a3a" d="M6.6 10.8c1.4 2.8 3.8 5.1 6.6 6.6l2.2-2.2c.3-.3.7-.4 1-.2 1.1.4 2.3.6 3.6.6.6 0 1 .4 1 1V20c0 .6-.4 1-1 1C10.6 21 3 13.4 3 4c0-.6.4-1 1-1h3.5c.6 0 1 .4 1 1 0 1.3.2 2.5.6 3.6.1.3 0 .7-.2 1z"/></svg></span>
  123 456 7890</div>
<a href="#" class="btn btn-green hero-btn abs">GET A QUOTE ➔</a>

<section class="band abs">
  <p class="band-text abs">Lorem Ipsum is simply dummy text.</p>
  <a href="#" class="btn btn-blue band-btn abs">CONTACT US ➔</a>
</section>

<h2 class="section-title services-title abs">SERVICES <span>WE PROVIDE</span></h2>
<p class="services-lead abs">Lorem Ipsum is dummy text of the printing and typesetting industry. Lorem Ipsum has been the industry's standard dummy text ever since the 1500s.</p>

<div class="service abs" style="left:72px"><div class="service-photo" role="img" aria-label="Photo of financial charts and a calculator"></div><h3>Equipment</h3><p>Lorem Ipsum is dummy text of the printing and typesetting industry.</p></div>
<div class="service abs" style="left:288px"><div class="service-photo" role="img" aria-label="Photo of stacked coins growing"></div><h3>Business</h3><p>Lorem Ipsum is dummy text of the printing and typesetting industry.</p></div>
<div class="service abs" style="left:504px"><div class="service-photo" role="img" aria-label="Photo of a business handshake"></div><h3>Commercial</h3><p>Lorem Ipsum is dummy text of the printing and typesetting industry.</p></div>
<div class="service abs" style="left:720px"><div class="service-photo" role="img" aria-label="Photo of a building under construction"></div><h3>Construction</h3><p>Lorem Ipsum is dummy text of the printing and typesetting industry.</p></div>
<div class="service abs" style="left:936px"><div class="service-photo" role="img" aria-label="Photo of a bridge over water"></div><h3>Bridging</h3><p>Lorem Ipsum is dummy text of the printing and typesetting industry.</p></div>

<section class="welcome abs">
  <p class="welcome-kicker abs">WELCOME TO</p>
  <h2 class="welcome-name abs">PETER LASKO-WREN FINANCE</h2>
  <p class="welcome-text abs">Lorem Ipsum is dummy text of the printing and typesetting industry. Lorem Ipsum has been the industry's standard dummy text ever since the 1500s, when an unknown printer took a galley of type it to make a type specimen book.</p>
  <a href="#" class="btn btn-green welcome-btn abs">READ MORE</a>
  <div class="video abs" role="img" aria-label="Video still of a city skyline at dusk">
    <svg class="play abs" width="60" height="60" viewBox="0 0 60 60"><circle cx="30" cy="30" r="29" fill="rgba(255,255,255,.85)"/><path d="M24 18l18 12-18 12z" fill="#2f3b4b"/></svg>
  </div>
</section>

<h2 class="col-title news-title abs">LATEST <span>NEWS</span></h2>
<article class="news-item abs" style="top:1858px">
  <div class="date"><b>09</b><small>JAN</small></div>
  <div class="news-body"><p>Lorem Ipsum is dummy text of the printing and typesetting industry. Lorem Ipsum has been...</p><a href="#">READ MORE »</a></div>
</article>
<article class="news-item abs" style="top:2018px">
  <div class="date"><b>09</b><small>JAN</small></div>
  <div class="news-body"><p>Lorem Ipsum is dummy text of the printing and typesetting industry. Lorem Ipsum has been...</p><a href="#">READ MORE »</a></div>
</article>

<h2 class="col-title quote-title abs">GET A <span>FREE QUOTE</span></h2>
<div class="field" style="left:628px;top:1856px;width:232px">Enter Name</div>
<div class="field" style="left:880px;top:1856px;width:248px">Enter Contact No.</div>
<div class="field" style="left:628px;top:1926px;width:500px">Enter Email</div>
<div class="field" style="left:628px;top:1994px;width:500px;height:118px">Enter Message</div>
<a href="#" class="btn btn-green submit abs">SUBMIT</a>

<footer class="footer abs">
  <nav class="footer-nav abs"><a href="#">Home</a><a href="#">About</a><a href="#">Services</a><a href="#">Contact</a></nav>
  <div class="social abs"><span></span><span></span><span></span></div>
  <div class="footer-rule abs"></div>
  <div class="contact-item abs" style="left:72px">
    <span class="dot"><svg width="20" height="22" viewBox="0 0 24 24"><path fill="#1c7bbb" d="M12 2a7 7 0 0 0-7 7c0 5 7 13 7 13s7-8 7-13a7 7 0 0 0-7-7zm0 9.5A2.5 2.5 0 1 1 12 6a2.5 2.5 0 0 1 0 5.5z"/></svg></span>
    <span>Lorem Ipsum is dummy<br>text of the printing.</span></div>
  <div class="contact-item big abs" style="left:340px">
    <span class="dot"><svg width="20" height="20" viewBox="0 0 24 24"><path fill="#1c7bbb" d="M6.6 10.8c1.4 2.8 3.8 5.1 6.6 6.6l2.2-2.2c.3-.3.7-.4 1-.2 1.1.4 2.3.6 3.6.6.6 0 1 .4 1 1V20c0 .6-.4 1-1 1C10.6 21 3 13.4 3 4c0-.6.4-1 1-1h3.5c.6 0 1 .4 1 1 0 1.3.2 2.5.6 3.6.1.3 0 .7-.2 1z"/></svg></span>
    <span>123 456 7890</span></div>
  <div class="contact-item abs" style="left:620px">
    <span class="dot"><svg width="20" height="16" viewBox="0 0 24 18"><rect x="1" y="1" width="22" height="16" fill="none" stroke="#1c7bbb" stroke-width="2"/><path d="M1 1l11 9 11-9" fill="none" stroke="#1c7bbb" stroke-width="2"/></svg></span>
    <span>info@peterlaskowren.com</span></div>
  <div class="contact-item abs" style="left:900px">
    <span>© <b>Peter Lasko-Wren</b> - 2017. All<br>Rights Reserved.</span></div>
</footer>

</body>
</html>
```